Velvor IT Services Business Card

Velvor IT Services are a Perth based IT Services company. We would like to incorporate our company logo (attached) and stick with the blue that is in that design. I would like a clean look design that isn't too busy, yet creates a lasting image that is instantly recognisable in the recipients mind.

Target Market(s)

The target audience is small/medium business owners.

Industry/Entity Type

Business

Font styles to use
Serif
Sans Serif

Colors

Designer to choose colors to be used in the design.

Requirements
Must have
• The design should include:
Business name: Velvor IT Services
Directors Name: Marcus Dredge
Phone Number: 0483 906 452
Email: support@velvorit.com.au
Website: www.velvorit.com.au

```html
<!DOCTYPE html>
<html lang="en">
<head>
<meta charset="utf-8">
<title>Velvor IT Services – Business Card</title>
<link href="https://fonts.googleapis.com/css2?family=Lato:ital,wght@0,400;0,700;0,900;1,700&display=swap" rel="stylesheet">
<style>
  :root {
    --brand-deep: #1f4fa8;
    --brand-mid: #2f73c9;
    --brand-light: #45c3ef;
    --ink: #3a3a3a;
    --ink-soft: #555;
    --card: #ffffff;
    --backdrop: #e6e8ec;
  }
  * { box-sizing: border-box; margin: 0; padding: 0; }
  html, body {
    width: 1200px; height: 1000px; overflow: hidden;
    background: var(--backdrop);
    font-family: "Lato", Arial, sans-serif;
  }
  .sheet {
    width: 1200px; height: 1000px;
    display: flex; flex-direction: column; align-items: center; justify-content: center;
    gap: 44px;
  }
  .card {
    width: 760px; height: 434px;
    background: var(--card);
    box-shadow: 0 10px 30px rgba(0,0,0,.18);
    position: relative; overflow: hidden;
  }

  /* wordmark */
  .wordmark { display: flex; align-items: center; gap: 14px; color: var(--brand-deep); font-weight: 900; }
  .wordmark__square { background: var(--brand-mid); flex: none; }
  .wordmark__name { text-transform: uppercase; line-height: 1; letter-spacing: .04em; }

  /* front */
  .card--front { display: flex; align-items: center; justify-content: center; }
  .card--front .wordmark__square { width: 54px; height: 54px; }
  .card--front .wordmark__name { font-size: 50px; }

  /* back */
  .card--back .wordmark { position: absolute; left: 52px; top: 56px; }
  .card--back .wordmark__square { width: 30px; height: 30px; }
  .card--back .wordmark__name { font-size: 28px; }

  .holder { position: absolute; left: 52px; top: 178px; }
  .holder__name { font-size: 25px; font-weight: 900; color: var(--brand-deep); text-transform: uppercase; letter-spacing: .01em; }
  .holder__role { font-size: 19px; color: var(--ink-soft); margin-top: 4px; }

  .contacts { position: absolute; left: 52px; top: 278px; list-style: none; }
  .contacts li { font-size: 20px; color: var(--ink); line-height: 31px; }
  .contacts b { color: var(--brand-deep); font-style: italic; font-weight: 700; margin-right: 4px; }

  .accent-block {
    position: absolute; right: 0; top: 0; width: 210px; height: 434px;
    background: linear-gradient(160deg, var(--brand-deep), var(--brand-mid) 55%, var(--brand-light));
  }
</style>
</head>
<body>
<main class="sheet">
  <section class="card card--front" aria-label="Card front">
    <div class="wordmark">
      <span class="wordmark__square"></span>
      <span class="wordmark__name">Velvor IT Services</span>
    </div>
  </section>

  <section class="card card--back" aria-label="Card back">
    <div class="wordmark">
      <span class="wordmark__square"></span>
      <span class="wordmark__name">Velvor IT Services</span>
    </div>
    <div class="holder">
      <p class="holder__name">Marcus Dredge</p>
      <p class="holder__role">Director</p>
    </div>
    <ul class="contacts">
      <li><b>P:</b> 0483 906 452</li>
      <li><b>E:</b> support@velvorit.com.au</li>
      <li><b>W:</b> www.velvorit.com.au</li>
    </ul>
    <div class="accent-block"></div>
  </section>
</main>
</body>
</html>
```